Checkout sign

Wall sign for clinic checkout.
“The Good Lord does ALL the healing..
But we DO collect the co-pay”

Add Celtic cross at top and our logo on bottom

```html
<!DOCTYPE html>
<html lang="en">
<head>
<meta charset="utf-8">
<title>Checkout Sign – Brennan Orthopedic Clinic</title>
<link href="https://fonts.googleapis.com/css2?family=Cinzel:wght@400;700&display=swap" rel="stylesheet">
<style>
  :root {
    --ink: #1c0a9c;
    --ink-soft: #d9d5f0;
    --sign: #ffffff;
    --backdrop: #e4e4e4;
  }
  * { box-sizing: border-box; margin: 0; padding: 0; }
  html, body {
    width: 1200px;
    height: 1200px;
    overflow: hidden;
    background: var(--backdrop);
  }
  .canvas {
    position: relative;
    width: 1200px;
    height: 1200px;
  }
  .sign {
    position: absolute;
    left: 123px;
    top: 30px;
    width: 954px;
    height: 1140px;
    background: var(--sign);
    border-radius: 68px;
    font-family: "Cinzel", "Trajan Pro", serif;
    color: var(--ink);
  }
  .sign__frame-outer {
    position: absolute;
    inset: 19px;
    border: 9px solid var(--ink);
    border-radius: 56px;
  }
  .sign__frame-inner {
    position: absolute;
    inset: 49px;
    border: 2.5px solid var(--ink);
    border-radius: 44px;
  }
  .sign__cross {
    position: absolute;
    left: 326px;
    top: 70px;
    width: 302px;
    height: 302px;
    background: radial-gradient(circle, #b9b2e4 0%, var(--ink-soft) 70%);
    border-radius: 8px;
  }
  .sign__message {
    position: absolute;
    left: 0;
    right: 0;
    top: 410px;
    text-align: center;
    line-height: 64px;
  }
  .sign__message .line { display: block; }
  .line--lead { font-size: 52px; font-weight: 700; }
  .line--body { font-size: 46px; font-weight: 400; }
  .line--close { font-size: 46px; font-weight: 700; }
  .brand {
    position: absolute;
    left: 0;
    right: 0;
    top: 706px;
    text-align: center;
  }
  .brand__mark {
    display: block;
    margin: 0 auto;
    width: 236px;
    height: 236px;
  }
  .brand__name {
    display: block;
    margin-top: 14px;
    font-size: 74px;
    font-weight: 400;
    line-height: 80px;
    letter-spacing: 1px;
  }
  .brand__tagline {
    display: block;
    font-size: 30px;
    font-weight: 400;
    line-height: 36px;
    letter-spacing: 1px;
  }
</style>
</head>
<body>
<div class="canvas">
  <div class="sign">
    <div class="sign__frame-outer"></div>
    <div class="sign__frame-inner"></div>

    <div class="sign__cross" role="img" aria-label="Celtic cross with interlaced knotwork and ring"></div>

    <p class="sign__message">
      <span class="line line--lead">The Good Lord</span>
      <span class="line line--body">does ALL the healing..</span>
      <span class="line line--body">But we DO collect</span>
      <span class="line line--close">the co-pay</span>
    </p>

    <div class="brand">
      <svg class="brand__mark" viewBox="0 0 236 236" aria-hidden="true">
        <circle cx="118" cy="118" r="110" fill="none" stroke="var(--ink)" stroke-width="8"/>
      </svg>
      <span class="brand__name">Brennan</span>
      <span class="brand__tagline">Orthopedic Clinic</span>
    </div>
  </div>
</div>
</body>
</html>
```